House-share and Room Rental Website (With Focus on the Bedroom Landing Page)

Looking for website design for our House-share (executive accommodation) and room rental business.

Our company name is: Lodvenra could also be written as LodVenra or lodvenra. Either is fine .. just looking for a nice clean catchy logo to go with the design.

EXAMPLES
These are examples of other websites in this field that are doing well. this is a kind of baseline.
https://kelbrin.com.au/
https://www.tuvaplex.com/
https://www.nestorvi.com/
https://www.quillsa.net/
https://www.pendlebarrow.com.au/

Our business model is to rent rooms to people looking for high-quality accommodation. We fill the gap between those looking to rent rooms and those with rooms to rent. However, our model is slightly different from those already on the market as we looking to fill a massive gap in the market delivering upmarket rooms for rent.(Executive Accommodation) also in the back end will be coupled with a self management process in the back end.

We offer executive style accommodation that stands out above the rest. With special extras like fire safety.. and management processes that create happier homes. We are looking for a web design package that can help us grow and scale our business. We need a design that is captivating

Our MAIN focus is having a room landing page that stands out from the rest... The core of our business will rely on the promotion of the rooms in a share house... so the whole design relies on the BEDROOM landing page to drive results.

Target Market(s)

We have 2 markets we are aiming at ... the first market is people offering rooms to rent who want the highest rental return. The second market is people looking to rent safe, high-quality rooms, in houses that are well managed and looked after.

Industry/Entity Type

Share Economy

Logo Text

LodVenra

Number of Pages Required

5+ page

Font styles to use
Sans Serif

Colors
3276b5

Requirements
Must have
• A messaging system whereby we can create direct communication between those offering rooms and those looking for rooms.
• A call to action that says " Schedule an Inspection"
• Landing page for promoting rooms
• A home page for showing stock.
• Profile page for those selling rooms
• Profile page for those looking for rooms.
• A scheduling calendar for booking inspections
Nice to have
• Pages where new residents can lock in a room.. pay bond and rents.. and sign contracts
• Notifications
• SMS capabilities in the backend.
Should not have
• No script or handwriting fonts.

```html
<!DOCTYPE html>
<html lang="en">
<head>
<meta charset="utf-8">
<title>Lodvenra – Executive Accommodation</title>
<link rel="stylesheet" href="https://fonts.googleapis.com/css2?family=Montserrat:wght@400;500;700;800&display=swap">
<style>
  :root {
    --brand-blue: #1b7fe2;
    --accent-orange: #ffab00;
    --ink: #1d1d1f;
    --ink-soft: #4a4a4a;
    --white: #ffffff;
    --wall-light: #f6f6f6;
    --wall-mid: #e9e9ea;
  }
  * { box-sizing: border-box; margin: 0; padding: 0; }
  html, body { width: 990px; height: 1200px; overflow: hidden; }
  body {
    position: relative;
    font-family: "Montserrat", Arial, sans-serif;
    color: var(--ink);
    background: var(--white);
  }
  .site-header {
    position: absolute; left: 0; top: 0; width: 990px; height: 44px;
    background: var(--white);
  }
  .brand { position: absolute; left: 138px; top: 6px; display: flex; align-items: center; gap: 6px; }
  .brand-dot { width: 31px; height: 31px; border-radius: 50%; background: var(--brand-blue); }
  .brand-name { font-size: 22px; font-weight: 400; line-height: 1; color: var(--ink); }
  .brand-tag { font-size: 8.5px; color: var(--ink-soft); margin-top: 2px; }
  .main-nav { position: absolute; top: 18px; font-size: 8px; font-weight: 500; color: var(--ink); }
  .nav-create { left: 686px; }
  .nav-login { left: 785px; }
  .menu-toggle { position: absolute; left: 832px; top: 16px; }

  .hero {
    position: absolute; left: 0; top: 44px; width: 990px; height: 458px; overflow: hidden;
  }
  .hero-photo {
    position: absolute; inset: 0;
    background:
      radial-gradient(ellipse 260px 160px at 540px 230px, rgba(168,176,172,0.95), rgba(168,176,172,0) 100%),
      radial-gradient(ellipse 200px 130px at 360px 250px, rgba(222,214,198,0.9), rgba(222,214,198,0) 100%),
      radial-gradient(ellipse 220px 200px at 820px 90px, rgba(236,238,236,0.95), rgba(236,238,236,0) 100%),
      radial-gradient(ellipse 120px 110px at 940px 110px, rgba(190,120,100,0.7), rgba(190,120,100,0) 100%),
      radial-gradient(ellipse 160px 200px at 90px 260px, rgba(176,150,112,0.9), rgba(176,150,112,0) 100%),
      radial-gradient(ellipse 260px 120px at 300px 120px, rgba(196,168,128,0.85), rgba(196,168,128,0) 100%),
      linear-gradient(180deg, #e2dbd0 0%, #cdbba0 30%, #bfa987 58%, #c9a27a 78%, #c8b196 100%);
  }
  .hero-title {
    position: absolute; left: 0; width: 990px; top: 185px;
    text-align: center; font-size: 25.5px; font-weight: 800; line-height: 37px;
    color: #232323; text-transform: uppercase;
  }
  .btn {
    position: absolute; display: flex; align-items: center; justify-content: center;
    background: var(--accent-orange); color: var(--white);
    font-weight: 800; text-transform: uppercase; text-decoration: none;
  }
  .btn-search { left: 386px; top: 290px; width: 216px; height: 51px; font-size: 16px; }

  .features {
    position: absolute; left: 0; top: 502px; width: 990px; height: 698px;
    background: linear-gradient(180deg, var(--white) 0%, var(--wall-light) 18%, #f2f2f2 60%, var(--wall-mid) 90%, #e4e4e5 100%);
  }
  .section-title {
    position: absolute; left: 0; width: 990px; text-align: center;
    color: var(--brand-blue); font-weight: 800; text-transform: uppercase;
  }
  .why-title { top: 40px; font-size: 18px; }
  .why-lead { position: absolute; left: 0; width: 990px; top: 77px; text-align: center; font-size: 15px; color: var(--ink); }

  .feature-frame { position: absolute; border: 3px solid var(--accent-orange); }
  .feature-photo { position: absolute; }
  .feature-name {
    position: absolute; font-size: 11px; font-weight: 700; text-transform: uppercase; color: var(--ink);
    white-space: nowrap;
  }
  .feature-rule { position: absolute; width: 24px; height: 2px; background: var(--accent-orange); }
  .feature-copy { position: absolute; font-size: 9.4px; line-height: 15px; color: var(--ink-soft); white-space: nowrap; }

  .offer-title { top: 426px; font-size: 22.7px; }
  .btn-inspection { left: 360px; top: 472px; width: 270px; height: 50px; font-size: 15px; }

  .social {
    position: absolute; top: 562px; width: 52px; height: 52px;
    border: 1.5px solid var(--ink); border-radius: 50%;
    display: flex; align-items: center; justify-content: center;
    font-size: 9px; font-weight: 700; color: var(--ink); text-decoration: none;
  }
  .copyright { position: absolute; left: 0; width: 990px; top: 668px; text-align: center; font-size: 8px; color: var(--ink); }
</style>
</head>
<body>
  <header class="site-header">
    <div class="brand">
      <span class="brand-dot"></span>
      <div>
        <div class="brand-name">Lodvenra</div>
        <div class="brand-tag">Executive Accommodation</div>
      </div>
    </div>
    <span class="main-nav nav-create">CREATE AN ACCOUNT</span>
    <span class="main-nav nav-login">LOGIN</span>
    <svg class="menu-toggle" width="18" height="14" viewBox="0 0 18 14" aria-label="Menu">
      <rect x="0" y="0" width="18" height="3" fill="#ffab00"/>
      <rect x="0" y="5.5" width="18" height="3" fill="#ffab00"/>
      <rect x="0" y="11" width="18" height="3" fill="#ffab00"/>
    </svg>
  </header>

  <section class="hero">
    <div class="hero-photo" role="img" aria-label="Bright loft bedroom with a wooden bed, grey bedding, lamps, brick wall and a patterned rug"></div>
    <h1 class="hero-title">High-quality accommodation<br>in a share house</h1>
    <a class="btn btn-search" href="#">Search for a room</a>
  </section>

  <section class="features">
    <h2 class="section-title why-title">Why Lodvenra is different</h2>
    <p class="why-lead">We offer bedrooms on rent that stands out above the rest.</p>

    <div class="feature-frame" style="left:147px;top:142px;width:201px;height:118px;"></div>
    <div class="feature-photo" role="img" aria-label="White executive bedroom with blue floral bedding" style="left:141px;top:136px;width:201px;height:119px;background:linear-gradient(135deg,#d9dee0,#9fb9bd 55%,#e8e4df);"></div>
    <h3 class="feature-name" style="left:142px;top:284px;">Executive rooms</h3>
    <span class="feature-rule" style="left:141px;top:304px;"></span>
    <p class="feature-copy" style="left:140px;top:312px;">Lorem ipsum dolor sit amet, consectetur<br>adipiscing elit. Proin rhoncus, erat fringilla<br>viverra egestas, risus massa lacinia felis,<br>eget faucibus est elit id enim.</p>

    <div class="feature-frame" style="left:400px;top:130px;width:201px;height:118px;"></div>
    <div class="feature-photo" role="img" aria-label="Ceiling smoke alarm above a softly blurred living room" style="left:394px;top:136px;width:201px;height:119px;background:linear-gradient(180deg,#e4e4e4,#c9ccd0 55%,#b9c3cc);"></div>
    <h3 class="feature-name" style="left:393px;top:284px;">Safty and security</h3>
    <span class="feature-rule" style="left:394px;top:304px;"></span>
    <p class="feature-copy" style="left:394px;top:312px;">Lorem ipsum dolor sit amet, consectetur<br>adipiscing elit. Proin rhoncus, erat fringilla<br>viverra egestas, risus massa lacinia felis,<br>eget faucibus est elit id enim.</p>

    <div class="feature-frame" style="left:654px;top:142px;width:201px;height:118px;"></div>
    <div class="feature-photo" role="img" aria-label="Bedroom with grey headboard and floral white bedding" style="left:648px;top:136px;width:201px;height:119px;background:linear-gradient(135deg,#e6e2dc,#c8c2b7 50%,#ece9ee);"></div>
    <h3 class="feature-name" style="left:644px;top:283px;">Great amenities</h3>
    <span class="feature-rule" style="left:650px;top:303px;"></span>
    <p class="feature-copy" style="left:649px;top:311px;">Lorem ipsum dolor sit amet, consectetur<br>adipiscing elit. Proin rhoncus, erat fringilla<br>viverra egestas, risus massa lacinia felis,<br>eget faucibus est elit id enim.</p>

    <h2 class="section-title offer-title">Would you like to offer your room?</h2>
    <a class="btn btn-inspection" href="#">Schedule an inspection</a>

    <a class="social" style="left:394px;" href="#">Vynlo</a>
    <a class="social" style="left:469px;" href="#">Talkit</a>
    <a class="social" style="left:545px;" href="#">Pelmo</a>

    <p class="copyright">copyright 2019 lodvenra.com All Righs Reserved.</p>
  </section>
</body>
</html>
```